Creative/innovative law firm website

A law firm website that immediately looks different from other law firm websites. We like the color scheme (dark background with warm, neutral colors) and simple, organic logos (trees, leaves, etc.) of this website: https://brambleworth.legal/

We'll be offering creative/innovative solutions to complex problems faced by state governments, industries, other law firms, and individuals. We're located in Montana (U.S.A.), and the outdoors is a huge part of our lives and identities.

We will need a home page, an "About Us" page with a separate subpage for each attorney (two attorneys), a blog or "Publications" page, a payment portal (which will integrate with Quillo), and a "Services" page.

```html
<!DOCTYPE html>
<html lang="en">
<head>
<meta charset="utf-8">
<title>Harlow &amp; Whitcombe P.C. — Attorney</title>
<link href="https://fonts.googleapis.com/css2?family=Cinzel:wght@400;500;600&family=Lato:wght@400;700&display=swap" rel="stylesheet">
<style>
:root{
  --header-bg:#131626;
  --crumb-bg:#181d30;
  --page-bg:#0f1322;
  --footer-bg:#000000;
  --text:#ffffff;
  --gold:#deb68c;
  --button:#c98c4e;
  --rule:#2a2d38;
}
*{margin:0;padding:0;box-sizing:border-box}
html,body{width:1200px;height:1039px;overflow:hidden;background:var(--page-bg);color:var(--text);font-family:'Lato',sans-serif}
.site-header{position:absolute;left:0;top:0;width:1200px;height:99px;background:var(--header-bg)}
.brand{position:absolute;left:160px;top:36px;font-family:'Cinzel',serif;font-size:21px;letter-spacing:.5px;white-space:nowrap}
.brand .accent{color:var(--gold)}
.main-nav a,.footer-nav a{position:absolute;color:var(--text);text-decoration:none;font-size:15px;white-space:nowrap}
.main-nav a{top:42px}
.nav-active{color:var(--gold)!important}
.caret{display:inline-block;width:0;height:0;border-left:3px solid transparent;border-right:3px solid transparent;border-top:3px solid currentColor;margin-left:5px;vertical-align:middle}
.pay-button{position:absolute;left:881px;top:30px;width:158px;height:37px;background:var(--button);color:var(--text);font-family:'Cinzel',serif;font-size:14px;display:flex;align-items:center;justify-content:center;letter-spacing:.5px;text-decoration:none}
.breadcrumb{position:absolute;left:0;top:99px;width:1200px;height:37px;background:var(--crumb-bg);display:flex;align-items:center;padding-left:164px;font-size:15px;gap:10px}
.breadcrumb .sep{font-size:14px}
.breadcrumb .current{color:var(--gold)}
.page-title{position:absolute;left:0;top:216px;width:1200px;display:flex;justify-content:center;align-items:center;gap:16px;font-family:'Cinzel',serif;font-size:36px;font-weight:500;letter-spacing:1px}
.page-title .line{width:56px;height:2px;background:var(--gold)}
.page-title .accent{color:var(--gold)}
.body-copy{font-size:15px;line-height:25.5px}
.col-text{position:absolute;left:162px;top:280px;width:420px}
.col-text p+p{margin-top:10px}
.portrait{position:absolute;left:622px;top:286px;width:417px;height:300px;border-radius:4px;background:linear-gradient(120deg,#8aa7c4 0%,#c7d2dc 45%,#3b3f48 60%,#b6bec6 100%)}
.full-text{position:absolute;left:162px;top:606px;width:880px}
.site-footer{position:absolute;left:0;top:793px;width:1200px;height:246px;background:var(--footer-bg)}
.footer-brand{position:absolute;left:160px;top:34px;font-family:'Cinzel',serif;font-size:30px;line-height:37px;text-align:center;letter-spacing:1px;font-weight:500}
.footer-brand .accent{color:var(--gold)}
.footer-nav a{top:63px}
.footer-rule{position:absolute;left:160px;top:144px;width:879px;height:1px;background:var(--rule)}
.copyright{position:absolute;left:160px;top:186px;font-size:15px}
.copyright .accent{color:var(--gold);font-weight:700}
.social{position:absolute;left:935px;top:180px}
</style>
</head>
<body>
<header class="site-header">
  <div class="brand"><span class="accent">Harlow &amp;</span> Whitcombe P.C.</div>
  <nav class="main-nav">
    <a style="left:489px" href="#">Home</a>
    <a style="left:552px" href="#">About</a>
    <a class="nav-active" style="left:616px" href="#">Our Attorneys<span class="caret"></span></a>
    <a style="left:745px" href="#">Services</a>
    <a style="left:824px" href="#">Blog</a>
  </nav>
  <a class="pay-button" href="#">Make Payment &nbsp;&gt;&gt;</a>
</header>

<div class="breadcrumb">
  <span>Home</span><span class="sep">»</span><span>Our Attorneys</span><span class="sep">»</span><span class="current">Lorem Ipsum Dolar Sit</span>
</div>

<h1 class="page-title"><span class="line"></span><span>Lorem Ipsum <span class="accent">Dolar sit</span></span><span class="line"></span></h1>

<div class="col-text body-copy">
  <p>Lorem ipsum dolor sit amet, consectetur adipiscing elit, sed do eiusmod tempor incididunt ut labore et dolore magna aliqua. Ut enim ad minim veniam, quis nostrud exercitation ullamco laboris nisi ut aliquip ex ea commodo consequat. Duis aute irure dolor in reprehenderit in voluptate velit esse cillum dolore eu fugiat nulla pariatur. Excepteur sint occaecat cupidatat non proident, sunt in culpa qui officia deserunt mollit anim id est laborum.</p>
  <p>Lorem ipsum dolor sit amet, consectetur adipiscing elit, sed do eiusmod tempor incididunt ut labore et dolore magna aliqua. Ut enim ad minim veniam, quis nostrud exercitation ullamco. sed do eiusmod tempor incididunt ut labore et dolore magna aliqua Ut enim ad minim veniam, quis nostrud exercitation ullamco</p>
</div>
<div class="portrait" role="img" aria-label="Portrait of the attorney in a dark suit standing before a glass office building"></div>

<p class="full-text body-copy">Lorem ipsum dolor sit amet, consectetur adipiscing elit, sed do eiusmod tempor incididunt ut labore et dolore magna aliqua. Ut enim ad minim veniam, quis nostrud exercitation ullamco laboris nisi ut aliquip ex ea commodo consequat. Duis aute irure dolor in reprehenderit in voluptate velit esse cillum dolore eu fugiat nulla pariatur. Excepteur sint occaecat cupidatat non proident, sunt in culpa qui officia deserunt mollit anim id est laborum.</p>

<footer class="site-footer">
  <div class="footer-brand"><span class="accent">Harlow &amp;</span><br>Whitcombe P.C.</div>
  <nav class="footer-nav">
    <a style="left:564px" href="#">Home</a>
    <a style="left:653px" href="#">About</a>
    <a class="nav-active" style="left:743px" href="#">Our Attorneys<span class="caret"></span></a>
    <a style="left:898px" href="#">Services</a>
    <a style="left:1000px" href="#">Blog</a>
  </nav>
  <div class="footer-rule"></div>
  <p class="copyright">Copyright 2021 <span class="accent">Harlow &amp; Whitcombe P.C.</span> All Rights Reserved.</p>
  <svg class="social" width="104" height="31" viewBox="0 0 104 31" role="img" aria-label="Social media links">
    <circle cx="15" cy="15.5" r="14.5" fill="#ffffff"/>
    <circle cx="15" cy="15.5" r="3" fill="#000000"/>
    <circle cx="52" cy="15.5" r="14" fill="none" stroke="#deb68c" stroke-width="1.2"/>
    <circle cx="52" cy="15.5" r="3" fill="#deb68c"/>
    <circle cx="89" cy="15.5" r="14" fill="none" stroke="#deb68c" stroke-width="1.2"/>
    <circle cx="89" cy="15.5" r="3" fill="#deb68c"/>
  </svg>
</footer>
</body>
</html>
```